I need two seperate flyers made
I have supplied 2 x photos of bathrooms, one for each flyer.
First flyer i want a banner or some sort of blockout acccross the bottom with my business name Marlow Bathrooms and my number 0487650923 and the promo is '' Renovate your bathroom from $10990 and in small writing under neath say owner to supply fixtures and tiles

Second flyer to have the same banner accross bottom and the promo is
Complete bathroom renovations from $15990 with small writing under saying terms and conditions apply

Want these to look professional and eye cathcing to generate more work.

I have attached 2x of our old flyers for reference and our current logo for use
Looking forward to working with you.

```html
<!DOCTYPE html>
<html lang="en">
<head>
<meta charset="utf-8">
<title>Marlow Bathrooms Flyers</title>
<link href="https://fonts.googleapis.com/css2?family=Montserrat:wght@300;400;500;600;700;800;900&display=swap" rel="stylesheet">
<style>
  :root {
    --backdrop: #a4a4a4;
    --ink-black: #070707;
    --brand-blue: #0b6fc1;
    --brand-blue-deep: #0a4f92;
    --white: #ffffff;
  }
  * { box-sizing: border-box; margin: 0; padding: 0; }
  html, body { width: 802px; height: 1200px; overflow: hidden; }
  body {
    background: var(--backdrop);
    font-family: "Montserrat", Arial, sans-serif;
    position: relative;
  }
  .flyer-set {
    position: absolute;
    top: 345px; left: 26px;
    display: flex; gap: 30px;
  }
  .flyer {
    position: relative;
    width: 360px; height: 510px;
    background: var(--ink-black);
    overflow: hidden;
    box-shadow: 10px 14px 18px rgba(0,0,0,0.45);
  }
  .flyer__photo { position: absolute; inset: 0; }
  .flyer__photo--shower {
    background:
      linear-gradient(to right, rgba(0,0,0,0) 60%, rgba(120,105,90,0.35) 85%, rgba(60,55,50,0.5) 100%),
      linear-gradient(to bottom, #080808 0%, #0b0b0b 17%, #4a4946 28%, #b9b6b0 45%, #cfccc6 58%, #8f8c86 72%, #262625 83%, #050505 92%);
  }
  .flyer__photo--vanity {
    background:
      radial-gradient(ellipse 60px 70px at 42% 48%, rgba(230,235,240,0.55), rgba(0,0,0,0) 70%),
      linear-gradient(to bottom, #080808 0%, #0b0b0b 17%, #3c3f42 28%, #a9adb0 44%, #c2c5c7 58%, #8c8f91 71%, #262728 83%, #050505 92%);
  }
  .headline {
    position: absolute; top: 34px; left: 0; right: 0;
    text-align: center; color: var(--white);
  }
  .headline__kicker {
    font-weight: 300; font-size: 17px; letter-spacing: 0.42em;
    margin-right: -0.42em; line-height: 1;
  }
  .headline__kicker--small { font-size: 13.5px; letter-spacing: 0.38em; }
  .headline__main {
    font-weight: 900; color: var(--brand-blue);
    font-size: 37px; line-height: 1; margin-top: 6px; letter-spacing: 0.01em;
  }
  .headline__main--long { font-size: 28.5px; margin-top: 5px; }
  .headline__note {
    font-weight: 500; font-size: 7px; letter-spacing: 0.33em;
    margin-right: -0.33em; margin-top: 8px;
  }
  .price-ribbon {
    position: absolute; top: 118px; left: 118px; width: 124px; height: 76px;
  }
  .price-ribbon svg { position: absolute; inset: 0; }
  .price-ribbon__text {
    position: absolute; top: 6px; left: 0; right: 10px;
    text-align: center; color: var(--white); line-height: 1;
    transform: rotate(-4deg);
  }
  .price-ribbon__from { display: block; font-weight: 700; font-size: 11px; padding-left: 54px; }
  .price-ribbon__amount { display: block; font-weight: 800; font-size: 21px; margin-top: 1px; }
  .contact-band {
    position: absolute; left: 0; right: 0; bottom: 0; height: 100px;
    text-align: center;
  }
  .brand-name {
    color: var(--brand-blue); font-weight: 500; line-height: 1; margin-top: 14px;
  }
  .brand-name__word { display: block; font-size: 26px; letter-spacing: 0.04em; }
  .brand-name__sub { display: block; font-size: 11px; letter-spacing: 0.5em; margin-right: -0.5em; margin-top: 6px; }
  .phone {
    display: inline-flex; align-items: center; gap: 6px;
    margin-top: 12px; color: var(--white);
    font-weight: 600; font-size: 13px; letter-spacing: 0.12em; line-height: 1;
  }
  .phone svg { width: 12px; height: 12px; }
</style>
</head>
<body>
  <div class="flyer-set">
    <article class="flyer">
      <div class="flyer__photo flyer__photo--shower" role="img" aria-label="Photo of a renovated bathroom with white tiles, oval mirror, floating white vanity and brass rain shower behind a glass screen"></div>
      <div class="headline">
        <p class="headline__kicker">RENOVATE YOUR</p>
        <h1 class="headline__main">BATHROOM</h1>
        <p class="headline__note">OWNER TO SUPPLY FIXTURES AND TILES</p>
      </div>
      <div class="price-ribbon">
        <svg viewBox="0 0 124 76" width="124" height="76">
          <polygon class="ribbon-tail" points="70,48 118,44 114,56 62,72" fill="var(--brand-blue-deep)"/>
          <polygon class="ribbon-body" points="0,14 121,0 120,42 4,48" fill="var(--brand-blue)"/>
        </svg>
        <p class="price-ribbon__text">
          <span class="price-ribbon__from">From</span>
          <span class="price-ribbon__amount">$10990</span>
        </p>
      </div>
      <footer class="contact-band">
        <p class="brand-name">
          <span class="brand-name__word">MARLOW</span>
          <span class="brand-name__sub">BATHROOMS</span>
        </p>
        <p class="phone">
          <svg viewBox="0 0 24 24" aria-hidden="true"><path fill="var(--brand-blue)" d="M6.6 10.8a15.2 15.2 0 0 0 6.6 6.6l2.2-2.2a1 1 0 0 1 1-.25 11.4 11.4 0 0 0 3.6.57 1 1 0 0 1 1 1V20a1 1 0 0 1-1 1A17 17 0 0 1 3 4a1 1 0 0 1 1-1h3.5a1 1 0 0 1 1 1c0 1.25.2 2.45.57 3.57a1 1 0 0 1-.25 1z"/></svg>
          0487650923
        </p>
      </footer>
    </article>

    <article class="flyer">
      <div class="flyer__photo flyer__photo--vanity" role="img" aria-label="Photo of a renovated bathroom with a backlit round mirror, white shaker vanity, freestanding bath and pendant light"></div>
      <div class="headline">
        <p class="headline__kicker headline__kicker--small">COMPLETE BATHROOM</p>
        <h1 class="headline__main headline__main--long">RENOVATIONS</h1>
        <p class="headline__note">TERMS AND CONDITIONS APPLY</p>
      </div>
      <div class="price-ribbon" style="top:112px;">
        <svg viewBox="0 0 124 76" width="124" height="76">
          <polygon class="ribbon-tail" points="70,48 118,44 114,56 62,72" fill="var(--brand-blue-deep)"/>
          <polygon class="ribbon-body" points="0,14 121,0 120,42 4,48" fill="var(--brand-blue)"/>
        </svg>
        <p class="price-ribbon__text">
          <span class="price-ribbon__from">From</span>
          <span class="price-ribbon__amount">$15990</span>
        </p>
      </div>
      <footer class="contact-band">
        <p class="brand-name">
          <span class="brand-name__word">MARLOW</span>
          <span class="brand-name__sub">BATHROOMS</span>
        </p>
        <p class="phone">
          <svg viewBox="0 0 24 24" aria-hidden="true"><path fill="var(--brand-blue)" d="M6.6 10.8a15.2 15.2 0 0 0 6.6 6.6l2.2-2.2a1 1 0 0 1 1-.25 11.4 11.4 0 0 0 3.6.57 1 1 0 0 1 1 1V20a1 1 0 0 1-1 1A17 17 0 0 1 3 4a1 1 0 0 1 1-1h3.5a1 1 0 0 1 1 1c0 1.25.2 2.45.57 3.57a1 1 0 0 1-.25 1z"/></svg>
          0487650923
        </p>
      </footer>
    </article>
  </div>
</body>
</html>
```